Plumbing company needs a brochure design

KRW Plant Solutions is a mechanical services plumbing company that designs, installs, services and maintains commercial & industrial HVAC systems (heating, ventilation, air-conditioning systems manufactured by Velkor, Zorvath and Halvereno Thermal).
We would like a brochure that could be sent to prospects following a cold or warm call as a general introduction prior to a sales appointment.
We'd like to incorporate our 'breath clean air' campaign in the brochure as well. Details are on our website
The services we'd like to focus on the following services: Air conditioning; Design; Service & Maintenance; Air Filtration; and Refrigeration. No need to mention labour hire or trades & services
Our website is krwplantsolutions.example
Target Market(s)
Building and property managers; building owners; facility managers of restaurants; hospitals; aged care facilities; conference centres; shopping centres
Industry/Entity Type
Industrial
Requirements
Must have
- 4 pages; contact details on last page (same as listed on our 'Contact Us' page on website. Half fold

```html
<!DOCTYPE html>
<html lang="en">
<head>
<meta charset="utf-8">
<title>KRW Plant Solutions – Brochure Back Cover</title>
<link href="https://fonts.googleapis.com/css2?family=Roboto+Condensed:wght@400;700&display=swap" rel="stylesheet">
<style>
  :root{
    --navy:#0d3b7a;
    --orange:#f47a12;
    --blue-bright:#1560d6;
    --white:#ffffff;
    --page-bg:#e9e9e9;
  }
  *{box-sizing:border-box;margin:0;padding:0}
  html,body{width:1200px;height:900px;overflow:hidden;background:var(--page-bg);
    font-family:"Roboto Condensed",Arial,sans-serif}
  .cover{position:absolute;left:90px;top:88px;width:1020px;height:727px;overflow:hidden;background:var(--navy)}
  .cover-shapes{position:absolute;inset:0}
  .contact-pill{position:absolute;left:172px;top:375px;width:120px;height:32px;border-radius:16px;
    background:var(--white);color:var(--navy);font-weight:700;font-size:18px;
    display:flex;align-items:center;justify-content:center;letter-spacing:.3px}
  .office{position:absolute;color:var(--white);font-size:11.5px;font-weight:700;line-height:14.2px}
  .office-title{display:flex;align-items:center;gap:10px;margin-left:-29px;
    color:var(--orange);font-size:15.5px;margin-bottom:4px;line-height:18px}
  .office-title svg{width:18px;height:16px;fill:var(--white)}
  .office--mel{left:47px;top:436px}
  .office--per{left:308px;top:436px}
  .office--png{left:47px;top:513px}
  .office--chn{left:308px;top:513px}
  .phone-box{position:absolute;left:0;top:642px;width:342px;height:62px;background:var(--white);
    border-radius:0 6px 6px 0;display:flex;align-items:center;padding-left:47px;gap:13px}
  .phone-icon{width:37px;height:37px;background:var(--orange);border-radius:4px;display:flex;
    align-items:center;justify-content:center}
  .phone-icon svg{width:22px;height:22px;fill:var(--white)}
  .phone-number{color:var(--navy);font-weight:700;font-size:40px;letter-spacing:.5px}
  .brand-name{position:absolute;left:550px;top:472px;width:150px;display:flex;flex-direction:column;
    align-items:flex-start;gap:12px}
  .brand-mark{width:44px;height:44px;background:var(--white)}
  .brand-name span{color:var(--white);font-weight:700;font-size:33px;line-height:33px;text-transform:uppercase}
  .values{position:absolute;left:727px;top:527px;font-weight:700;text-transform:uppercase;line-height:1}
  .values div{margin-bottom:4px}
  .values .v-honesty{color:var(--white);font-size:55px}
  .values .v-reliability{color:var(--blue-bright);font-size:42px}
  .values .v-commitment{color:var(--white);font-size:38px}
  .website{position:absolute;left:653px;top:690px;color:var(--white);font-weight:700;font-size:16.5px;letter-spacing:1.6px}
</style>
</head>
<body>
<section class="cover">
  <svg class="cover-shapes" width="1020" height="727" viewBox="0 0 1020 727">
    <defs>
      <linearGradient id="siteGrad" x1="0" y1="0" x2="0.35" y2="1">
        <stop offset="0" stop-color="#c9ddf2"/>
        <stop offset=".18" stop-color="#b3cbe6"/>
        <stop offset=".3" stop-color="#8fa38a"/>
        <stop offset=".42" stop-color="#c2b9a8"/>
        <stop offset=".55" stop-color="#8e7e6c"/>
        <stop offset=".68" stop-color="#c9a93a"/>
        <stop offset=".8" stop-color="#7b7366"/>
        <stop offset="1" stop-color="#4f4c48"/>
      </linearGradient>
      <linearGradient id="techGrad" x1="0" y1="0" x2="1" y2="1">
        <stop offset="0" stop-color="#e6e8ea"/>
        <stop offset=".3" stop-color="#c9cdd2"/>
        <stop offset=".5" stop-color="#d9d63a"/>
        <stop offset=".72" stop-color="#2c3a5c"/>
        <stop offset="1" stop-color="#3c3f46"/>
      </linearGradient>
    </defs>
    <rect class="site-photo" role="img" aria-label="Crane lifting HVAC units onto a commercial building roof"
          x="0" y="0" width="1020" height="460" fill="url(#siteGrad)"/>
    <path class="orange-panel" fill="var(--orange)"
          d="M870,0 L1020,0 L1020,727 L510,727 L510,375 C700,360 900,382 975,290 C1012,230 995,80 870,0 Z"/>
    <path fill="none" stroke="var(--white)" stroke-width="4"
          d="M510,375 C700,360 900,382 975,290 C1012,230 995,80 870,0"/>
    <path class="navy-panel" fill="var(--navy)"
          d="M0,410 C150,340 350,320 510,375 L510,727 L0,727 Z"/>
    <path fill="none" stroke="var(--orange)" stroke-width="5"
          d="M0,410 C150,340 350,320 510,375"/>
    <rect class="footer-strip" x="510" y="680" width="510" height="47" fill="var(--navy)"/>
    <circle cx="832" cy="417" r="101" fill="var(--white)"/>
    <circle class="tech-photo" role="img" aria-label="Technician testing refrigerant gauges"
            cx="832" cy="417" r="96" fill="url(#techGrad)"/>
  </svg>

  <div class="contact-pill">CONTACT US</div>

  <div class="office office--mel">
    <div class="office-title"><svg viewBox="0 0 18 16"><path d="M9 0 18 8H15V16H11V11H7V16H3V8H0Z"/></svg>Melbourne, VIC</div>
    12 Tarrow Lane<br>Carlsworth 3010<br>Melbourne, VIC
  </div>
  <div class="office office--per">
    <div class="office-title"><svg viewBox="0 0 18 16"><path d="M9 0 18 8H15V16H11V11H7V16H3V8H0Z"/></svg>Perth, WA</div>
    27-31 Fenwick Drive<br>Belmont Hills 6118<br>Perth, WA
  </div>
  <div class="office office--png">
    <div class="office-title"><svg viewBox="0 0 18 16"><path d="M9 0 18 8H15V16H11V11H7V16H3V8H0Z"/></svg>Papua New Guinea</div>
    KRW Plant Solutions (PNG) Limited<br>Kestrel House<br>Ground Floor<br>Marlin Street<br>Port Moresby, PNG
  </div>
  <div class="office office--chn">
    <div class="office-title"><svg viewBox="0 0 18 16"><path d="M9 0 18 8H15V16H11V11H7V16H3V8H0Z"/></svg>China</div>
    No. 512<br>Building 8<br>Lanfeng Garden<br>Haiyue Road<br>Qinglin Town<br>Songhe Guangdong CHINA
  </div>

  <div class="phone-box">
    <div class="phone-icon"><svg viewBox="0 0 24 24"><path d="M6.6 10.8c1.4 2.8 3.8 5.1 6.6 6.6l2.2-2.2c.3-.3.7-.4 1-.2 1.1.4 2.3.6 3.6.6.6 0 1 .4 1 1V20c0 .6-.4 1-1 1C10.6 21 3 13.4 3 4c0-.6.4-1 1-1h3.5c.6 0 1 .4 1 1 0 1.3.2 2.5.6 3.6.1.3 0 .7-.2 1z"/></svg></div>
    <div class="phone-number">1300 555 014</div>
  </div>

  <div class="brand-name">
    <div class="brand-mark"></div>
    <span>KRW<br>Plant<br>Solutions</span>
  </div>

  <div class="values">
    <div class="v-honesty">Honesty</div>
    <div class="v-reliability">Reliability</div>
    <div class="v-commitment">Commitment</div>
  </div>

  <div class="website">www.krwplantsolutions.example</div>
</section>
</body>
</html>
```